Sharper Daily Habits Qorafone App

I am looking to create an Qorafone app (support Qorafone 5 and above) that will inspire and empower the app user to be more productive through a creative, interative and simplistic user experience that teaches the 10 topics related to "Sharper Daily Habits". Please see attached zip files for the 10 topic as PDF files and 20 posters (20 jpg files) which include a quote related to the content bundle’s topic.

Target Market(s)

working professionals who desire to be more productive in their ways of doing

Industry/Entity Type

It Support

Font styles to use
Sans Serif

Colors
33a6d7
0255a3
9bcb3b
cadf82
33b8a4

Requirements
Must have
• don't really wanna say "ebook" style app which would be below my expectation, i expect something more creative than an "ebook" app. i prefer you use your creativity to come up with the design but if you are a bit lost, please read below.
• some specs in my mind:
• - 10 flash cards design for each of the topic so they can be used in a carousel style menu (see sample app screenshot 1 - 1st screen to the left)
• - when presenting a topic, the background should be the same as the flash card of the topic (see sample app screenshot 2 - the right most screen)
• - at the bottom of the topic screen, a audio play/pause buttons bar should be presented as the app will play audible version for the article.
• - the fashion of the sample app screen shots shouldn't be followed as it is an ancient fashion reflecting the content. I expect the fashion of the app should be modern and reflect the topic "sharper daily habits"
• Screens required:
• - Main menu screen: carosoul style presenting the 10 topics using flash cards, should have a "play/pause" button to play the audible topic
• - Topic screen: presents the text content of the topic with flash card design as the background, paging buttons when content spans over one page, have media player bar at bottom to "play/pause/fast forward/reverse" audible
Nice to have
• i have 20 posters with quotes that inspires the user. i would like to see the posters to be presented full screen with a "inspire me" button somewhere which will randomly display a poster to the user.

```html
<!DOCTYPE html>
<html lang="en">
<head>
<meta charset="utf-8">
<title>Sharper Daily Habits – Topic Carousel</title>
<link rel="stylesheet" href="https://fonts.googleapis.com/css2?family=Arimo:wght@400;700&display=swap">
<style>
  :root {
    --page-bg: #ffffff;
    --brand-blue: #0a55a3;
    --stage-dark: #2a2a2a;
    --stage-deep: #1c1c1c;
    --text-light: #ffffff;
    --text-dark: #111111;
    --pill-line: rgba(255, 255, 255, 0.55);
    --player-bg: #ffffff;
    --card-haze: #d6d2ce;
    --card-accent: #e8c23a;
    --card-hair: #a88d62;
    --card-shadow: #1f1b18;
  }
  * { box-sizing: border-box; margin: 0; padding: 0; }
  html, body {
    width: 1200px; height: 1000px; overflow: hidden;
    background: var(--page-bg);
    font-family: "Arimo", Arial, sans-serif;
  }
  .screen {
    position: absolute; left: 389px; top: 126px;
    width: 420px; height: 744px;
    background: var(--stage-dark);
    overflow: hidden;
  }
  .status-bar {
    position: absolute; left: 0; top: 0; width: 100%; height: 26px;
    background: var(--brand-blue); color: var(--text-light);
    font-size: 13px; font-weight: 700;
    display: flex; align-items: center; justify-content: space-between;
    padding: 0 8px 0 10px;
  }
  .status-bar .signal { display: flex; align-items: center; gap: 2px; }
  .status-bar .signal i { width: 6px; height: 6px; border-radius: 50%; background: var(--text-light); display: block; }
  .status-bar .battery { display: flex; align-items: center; gap: 4px; }
  .status-bar .clock { position: absolute; left: 0; right: 0; text-align: center; pointer-events: none; }
  .nav-bar {
    position: absolute; left: 0; top: 26px; width: 100%; height: 53px;
    background: var(--brand-blue); color: var(--text-light);
  }
  .nav-bar .app-name {
    position: absolute; left: 0; right: 0; top: 15px; line-height: 34px;
    text-align: center; font-size: 18px; font-weight: 700; letter-spacing: 0.3px;
  }
  .nav-bar .menu-icon { position: absolute; right: 18px; top: 22px; }
  .stage {
    position: absolute; left: 0; top: 79px; width: 100%; height: 605px;
    background:
      radial-gradient(ellipse 60% 40% at 50% 95%, #3a342d 0%, transparent 100%),
      radial-gradient(ellipse at 50% 70%, #343230 0%, var(--stage-dark) 50%, var(--stage-deep) 100%);
  }
  .topic-title {
    position: absolute; left: 0; right: 0; top: 32px;
    text-align: center; color: var(--text-light);
    font-size: 24px; font-weight: 700; letter-spacing: 0.2px;
  }
  .flash-card {
    position: absolute; border-radius: 14px; overflow: hidden;
  }
  .flash-card.current {
    left: 78px; top: 92px; width: 260px; height: 408px;
    background:
      radial-gradient(ellipse 30% 14% at 92% 8%, var(--card-accent) 0%, transparent 100%),
      radial-gradient(ellipse 20% 30% at 8% 40%, #c98f86 0%, transparent 100%),
      radial-gradient(ellipse 70% 45% at 50% 55%, var(--card-hair) 0%, transparent 100%),
      radial-gradient(ellipse 60% 25% at 50% 100%, var(--card-shadow) 0%, transparent 100%),
      linear-gradient(180deg, var(--card-haze) 0%, #c9bfb2 25%, #8c7656 60%, #4a3d2e 85%, #2a2420 100%);
  }
  .flash-card.prev {
    left: -14px; top: 118px; width: 59px; height: 348px;
    background: linear-gradient(180deg, #2e2518 0%, #8a6a2e 45%, #4b3a1c 70%, #1e1a14 100%);
  }
  .flash-card.next {
    left: 375px; top: 118px; width: 59px; height: 348px;
    background: linear-gradient(180deg, #2a2a2c 0%, #7c7f86 40%, #3a3b3f 70%, #1d1d1f 100%);
  }
  .play-now {
    position: absolute; left: 139px; top: 528px; width: 148px; height: 40px;
    border: 1.5px solid var(--pill-line); border-radius: 20px;
    display: flex; align-items: center; justify-content: center; gap: 12px;
    color: var(--text-light); font-size: 17px; font-weight: 700;
  }
  .player-bar {
    position: absolute; left: 0; top: 684px; width: 100%; height: 60px;
    background: var(--player-bg);
  }
  .player-bar .pause { position: absolute; left: 12px; top: 20px; }
  .player-bar .track {
    position: absolute; left: 0; right: 0; top: 0; line-height: 56px;
    text-align: center; font-size: 17px; font-weight: 700; color: var(--text-dark);
  }
  .player-bar .more { position: absolute; right: 20px; top: 26px; }
  .player-bar .progress {
    position: absolute; left: 0; bottom: 1px; width: 296px; height: 2px;
    background: var(--brand-blue);
  }
</style>
</head>
<body>
  <main class="screen">
    <div class="status-bar">
      <span class="signal"><i></i><i></i><i></i><i></i><i></i>
        <svg width="14" height="10" viewBox="0 0 14 10" aria-hidden="true"><path d="M1 3.5a9 9 0 0 1 12 0M3.2 5.8a6 6 0 0 1 7.6 0M5.4 8a2.6 2.6 0 0 1 3.2 0" fill="none" stroke="#fff" stroke-width="1.6" stroke-linecap="round"/></svg>
      </span>
      <span class="clock">9:41 AM</span>
      <span class="battery">100%
        <svg width="28" height="12" viewBox="0 0 28 12" aria-hidden="true"><rect x="0.75" y="0.75" width="23.5" height="10.5" rx="2" fill="none" stroke="#fff" stroke-width="1.5"/><rect x="2.5" y="2.5" width="20" height="7" rx="1" fill="#fff"/><rect x="25.5" y="4" width="2" height="4" rx="1" fill="#fff"/></svg>
      </span>
    </div>

    <header class="nav-bar">
      <h1 class="app-name">HABITLIFT</h1>
      <svg class="menu-icon" width="26" height="18" viewBox="0 0 26 18" aria-label="Menu">
        <g fill="#fff">
          <rect x="0" y="1" width="3" height="1.6"/><rect x="5" y="1" width="21" height="1.6"/>
          <rect x="0" y="6" width="3" height="1.6"/><rect x="5" y="6" width="21" height="1.6"/>
          <rect x="0" y="11" width="3" height="1.6"/><rect x="5" y="11" width="21" height="1.6"/>
          <rect x="0" y="16" width="3" height="1.6"/><rect x="5" y="16" width="21" height="1.6"/>
        </g>
      </svg>
    </header>

    <section class="stage">
      <h2 class="topic-title">WORK HAPPY</h2>
      <div class="flash-card prev" role="img" aria-label="Flash card photo: warm golden close-up of a gift bow"></div>
      <div class="flash-card current" role="img" aria-label="Work Happy flash card photo: smiling young woman with long blonde hair and glasses against a soft bright background"></div>
      <div class="flash-card next" role="img" aria-label="Flash card photo: dark metallic close-up"></div>
      <div class="play-now">
        <svg width="18" height="20" viewBox="0 0 18 20" aria-hidden="true"><path d="M2 2l14 8-14 8z" fill="none" stroke="#fff" stroke-width="2" stroke-linejoin="round"/></svg>
        <span>Play Now</span>
      </div>
    </section>

    <footer class="player-bar">
      <svg class="pause" width="14" height="18" viewBox="0 0 14 18" aria-label="Pause"><rect x="1" y="0" width="3.5" height="18" fill="var(--brand-blue)"/><rect x="9.5" y="0" width="3.5" height="18" fill="var(--brand-blue)"/></svg>
      <div class="track">Distraction</div>
      <svg class="more" width="20" height="5" viewBox="0 0 20 5" aria-label="More options"><g fill="var(--brand-blue)"><circle cx="2.5" cy="2.5" r="2.3"/><circle cx="10" cy="2.5" r="2.3"/><circle cx="17.5" cy="2.5" r="2.3"/></g></svg>
      <div class="progress"></div>
    </footer>
  </main>
</body>
</html>
```